Product label design needed for an odor removal line of products.

I need a label designed for an odor removal product line. There are eight additional odor removal products that I will need labels designed for so the winner will have additional work from me. I would like each of those products to have a similar look and feel in each one. This contest is for one of the products. The Breezeward Pod 385 (would love a better name if you are so inclined -many people know what it is by the 385). The no smell formula does not mask odors, it eliminates odors at their source . Also Reduces Allergens! Simply open silver packet and place in dispenser. Great for use in cars, near pet beds or litter boxes, near diaper pails -anywhere odors are a problem. Lasts 60-90 days. Safe to use. Other uses: Nursing homes, hotel rooms, locker rooms, teenage boy rooms, basements... Eco Friendly! No VOC's or phthalates! Do not consume. Keep out of reach of children and pets. Replace every 60-90 days. I put the picture of my logo , the product as it is packaged and a picture of the actual product and the dispenser it will go in. the package is 4x5 in silver packet with .25 seam on the side and .5 seam on the top and bottom. (Dispenser will have a label with reorder information on it. to be designed later) You do not have to put all information provided on the label. It is to be used as you see fit. I tend to like clean, bold designs but am open to all options. Prefer not to use word air freshener.

Target Market(s)

Men and women between 30-65

Industry/Entity Type

Cleaning Product

Font styles to use
Sans Serif

Colors
acd136
9bcb3c
ffffff

Requirements
Must have
• ability for concept/look to be used for a laundry product, smaller odor elimination pouch, odor removing canister and spray as well
Nice to have
• I like greens but am open to designers to decide
Should not have
• word air freshener

```html
<!DOCTYPE html>
<html lang="en">
<head>
<meta charset="utf-8">
<title>The Breezeward Pod 385 – Product Label</title>
<link rel="stylesheet" href="https://fonts.googleapis.com/css2?family=Barlow:wght@300;400;600&display=swap">
<style>
  :root {
    --frame-grey: #58585a;
    --panel-dark: #38383a;
    --label-white: #ffffff;
    --brand-green: #7dc242;
    --ink-grey: #5b5c60;
    --name-ink: #38383a;
  }
  html, body {
    margin: 0;
    padding: 0;
    width: 1022px;
    height: 1200px;
    overflow: hidden;
    background: var(--frame-grey);
  }
  .canvas {
    position: relative;
    width: 1022px;
    height: 1200px;
    background: var(--frame-grey);
    font-family: "Barlow", sans-serif;
  }
  .label {
    position: absolute;
    left: 108px;
    top: 97px;
    width: 805px;
    height: 1005px;
    background: var(--panel-dark);
    overflow: hidden;
  }
  .label__top-band {
    position: absolute;
    left: 0;
    top: 0;
    width: 100%;
    height: 312px;
    background: var(--label-white);
  }
  .brand-seal {
    position: absolute;
    left: 169px;
    top: 81px;
    width: 466px;
    height: 466px;
    border-radius: 50%;
    background: var(--label-white);
    display: flex;
    flex-direction: column;
    align-items: center;
    justify-content: center;
  }
  .brand-seal__name {
    margin: 0;
    font-family: "Barlow", sans-serif;
    font-weight: 600;
    font-size: 50px;
    line-height: 1.1;
    letter-spacing: 4px;
    color: var(--name-ink);
    text-align: center;
    text-transform: uppercase;
  }
  .product-title {
    position: absolute;
    left: 0;
    top: 585px;
    width: 100%;
    margin: 0;
    font-family: "Barlow", sans-serif;
    font-weight: 600;
    font-size: 76px;
    line-height: 81px;
    color: var(--brand-green);
    text-align: center;
    text-transform: uppercase;
  }
  .claim-pill {
    position: absolute;
    left: 130px;
    top: 778px;
    width: 545px;
    height: 49px;
    background: var(--label-white);
    border-radius: 40px 0 40px 0;
    display: flex;
    align-items: center;
    justify-content: center;
    font-weight: 300;
    font-size: 26px;
    color: var(--ink-grey);
    white-space: pre;
  }
  .usage-notes {
    position: absolute;
    left: 0;
    top: 853px;
    width: 100%;
    margin: 0;
    font-weight: 400;
    font-size: 23px;
    line-height: 31px;
    color: var(--label-white);
    text-align: center;
  }
</style>
</head>
<body>
  <div class="canvas">
    <section class="label">
      <div class="label__top-band"></div>
      <div class="brand-seal">
        <p class="brand-seal__name">Fernhollow<br>Home</p>
      </div>
      <h1 class="product-title">The Breezeward<br>Pod 385</h1>
      <div class="claim-pill">Eco Friendly!  | No VOC's or phthalates!</div>
      <p class="usage-notes">Keep out of reach of children and pets.<br>Replace every 60-90 days</p>
    </section>
  </div>
</body>
</html>
```